Beekeeper needs a label for honey jars

Ciao! I'm from Como Italy
I'm a hobbyist beekeeper and I produce honey for myself and my friends.
I've named my apiary "Teo di sole," a play on words between my nickname (Teo, from Matteo) and the Italian expression "Teo di sole," which translates to "a drizzle of honey" in English.
I need to create a label for my honey glass jars (250 gr and 500 gr).
I don't need a label for commercial purposes. I would like to include at least the name “Apicoltura Teo di sole", the type of honey (e.g., wildflower, acacia...) and a space for the production year, to be handwritten each year.
In the design some references to the world of bees.
For reference, attached a label with a style I like
Attached are the images of the selected jars and their measurements
Thanks and good job!

Target Market(s)

beekeeping, honey

Requirements
Nice to have
• I would like an elegant style with clean graphics.
Should not have
• Predominance of black color.

```html
<!DOCTYPE html>
<html lang="en">
<head>
<meta charset="utf-8">
<title>Apicoltura Teo di sole – Honey Jar Label</title>
<link rel="stylesheet" href="https://fonts.googleapis.com/css2?family=Marcellus&family=Montserrat:wght@400;500&display=swap">
<style>
  :root {
    --backdrop: #dcdcdc;
    --label-paper: #f4f4f2;
    --ink: #161616;
    --ink-soft: #3a3a3a;
    --comb-tone: #d6d6d2;
    --comb-tone-light: #ecece9;
    --flag-green: #0f9a3a;
    --flag-white: #ffffff;
    --flag-red: #c8141d;
  }
  * { margin: 0; padding: 0; box-sizing: border-box; }
  html, body {
    width: 1200px; height: 1200px; overflow: hidden;
    background: var(--backdrop);
  }
  .label {
    position: absolute; left: 50px; top: 232px;
    width: 1100px; height: 736px;
    background: var(--label-paper);
    overflow: hidden;
    font-family: "Montserrat", sans-serif;
    color: var(--ink);
  }
  .comb-area { position: absolute; left: 0; top: 0; width: 1100px; height: 736px; }
  .centered {
    position: absolute; left: 0; width: 100%;
    text-align: center; line-height: 1;
  }
  .est {
    position: absolute; top: 150px; font-size: 16px; font-weight: 500;
    letter-spacing: 0.55em; line-height: 1;
  }
  .est-left { left: 415px; }
  .est-right { left: 605px; }
  .bee-mark { position: absolute; left: 504px; top: 124px; }
  .flag {
    position: absolute; left: 503px; top: 225px;
    width: 97px; height: 9px; display: flex;
    border: 1px solid var(--ink-soft);
  }
  .flag span { flex: 1; }
  .flag .g { background: var(--flag-green); }
  .flag .w { background: var(--flag-white); }
  .flag .r { background: var(--flag-red); }
  .apiary { top: 272px; font-size: 22px; font-weight: 500; letter-spacing: 0.36em; padding-left: 0.36em; }
  .brand-name {
    top: 330px; font-family: "Marcellus", serif; font-size: 94px;
    letter-spacing: 0.01em; color: var(--ink);
  }
  .variety { top: 457px; font-size: 21px; font-weight: 500; letter-spacing: 0.42em; padding-left: 0.42em; }
  .divider { position: absolute; left: 512px; top: 513px; width: 76px; height: 3px; background: var(--ink); }
  .year-caption { top: 562px; font-size: 12px; font-weight: 500; letter-spacing: 0.6em; padding-left: 0.6em; }
  .year-line { position: absolute; left: 405px; top: 619px; width: 294px; height: 1px; background: var(--ink-soft); }
  .weight { top: 641px; font-size: 17px; font-weight: 500; letter-spacing: 0.3em; padding-left: 0.3em; }
</style>
</head>
<body>
  <main class="label">
    <svg class="comb-area" width="1100" height="736" viewBox="0 0 1100 736">
      <defs>
        <linearGradient id="comb-fade" x1="0" y1="0" x2="1" y2="1">
          <stop offset="0" stop-color="var(--comb-tone)"/>
          <stop offset="1" stop-color="var(--comb-tone-light)"/>
        </linearGradient>
      </defs>
      <polygon role="img" aria-label="Honeycomb pattern, upper left corner"
        points="0,0 539,0 505,54 415,82 395,137 300,165 297,192 200,220 190,246 150,246 92,219 92,165 48,137 0,110"
        fill="url(#comb-fade)"/>
      <polygon role="img" aria-label="Honeycomb pattern, lower right corner"
        points="1100,736 564,736 590,683 675,655 690,600 775,573 800,518 850,491 918,491 1000,518 1050,573 1100,628"
        fill="url(#comb-fade)"/>
    </svg>

    <span class="est est-left">SICE</span>
    <svg class="bee-mark" width="94" height="66" viewBox="0 0 94 66" role="img" aria-label="Engraved honeybee illustration">
      <ellipse cx="47" cy="33" rx="46" ry="31" fill="var(--comb-tone)"/>
    </svg>
    <span class="est est-right">2023</span>

    <div class="flag" aria-label="Italian flag"><span class="g"></span><span class="w"></span><span class="r"></span></div>

    <p class="centered apiary">APICOLTURA</p>
    <h1 class="centered brand-name">TEO DI SOLE</h1>
    <p class="centered variety">WILDFLOWER HONEY</p>
    <div class="divider"></div>
    <p class="centered year-caption">PRODUCTION YEAR</p>
    <div class="year-line"></div>
    <p class="centered weight">250 Gr</p>
  </main>
</body>
</html>
```